Business Card *

A business card design
Use the logo uploaded in the brief page.
You may use placeholders in your design layouts.
I will provide the actual business card details to the winning designer.

Logo
Place for contact info (name, title, phone, email, etc)

Requirements
Must have
• Logo

```html
<!DOCTYPE html>
<html lang="en">
<head>
<meta charset="utf-8">
<title>Harrowfield Business Card</title>
<link href="https://fonts.googleapis.com/css2?family=Arimo:wght@400;700&display=swap" rel="stylesheet">
<style>
  :root {
    --backdrop: #e3e3e3;
    --card: #1e1f20;
    --card-edge: #2a2b2c;
    --name-grey: #8a8a8a;
    --text-light: #c9c9c9;
    --accent-green: #3cb449;
    --divider: #5a5a5a;
    --brand-silver: #c4c4c4;
  }
  html, body {
    margin: 0;
    padding: 0;
    width: 1200px;
    height: 1200px;
    overflow: hidden;
    background: var(--backdrop);
    font-family: "Arimo", Arial, sans-serif;
  }
  .canvas {
    position: relative;
    width: 1200px;
    height: 1200px;
  }
  .card {
    position: absolute;
    left: 257px;
    width: 686px;
    height: 391px;
    background: linear-gradient(160deg, var(--card-edge) 0%, var(--card) 60%, #19191a 100%);
    box-shadow: 0 14px 26px rgba(0,0,0,0.35);
  }
  .card-front { top: 165px; }
  .card-back { top: 653px; }

  .identity {
    position: absolute;
    right: 348px;
    top: 162px;
    text-align: right;
  }
  .identity-name {
    margin: 0;
    font-size: 28px;
    font-weight: 700;
    color: var(--name-grey);
    line-height: 1;
  }
  .identity-title {
    margin: 6px 2px 0 0;
    font-size: 15px;
    color: var(--accent-green);
  }
  .divider {
    position: absolute;
    left: 352px;
    top: 149px;
    width: 1px;
    height: 75px;
    background: var(--divider);
  }
  .contact-list {
    position: absolute;
    left: 376px;
    top: 150px;
    margin: 0;
    padding: 0;
    list-style: none;
  }
  .contact-list li {
    display: flex;
    align-items: center;
    height: 19.5px;
    font-size: 15.5px;
    color: var(--text-light);
  }
  .contact-list svg {
    width: 12px;
    height: 12px;
    margin-right: 9px;
    fill: var(--text-light);
  }
  .address {
    position: absolute;
    left: 0;
    right: 0;
    top: 312px;
    text-align: center;
    font-size: 15.5px;
    color: var(--text-light);
  }
  .address svg {
    width: 11px;
    height: 14px;
    margin-right: 5px;
    vertical-align: -1px;
    fill: none;
    stroke: var(--text-light);
    stroke-width: 1.6;
  }

  .brand {
    position: absolute;
    left: 0;
    right: 0;
    top: 170px;
    display: flex;
    align-items: center;
    justify-content: center;
    gap: 14px;
  }
  .brand-dot {
    width: 30px;
    height: 30px;
    border-radius: 50%;
    background: var(--accent-green);
  }
  .brand-name {
    font-size: 42px;
    font-weight: 700;
    letter-spacing: 1px;
    color: var(--brand-silver);
  }
</style>
</head>
<body>
<main class="canvas">
  <section class="card card-front">
    <div class="identity">
      <p class="identity-name">Daniel Brooks</p>
      <p class="identity-title">President</p>
    </div>
    <div class="divider"></div>
    <ul class="contact-list">
      <li>
        <svg viewBox="0 0 24 24" aria-hidden="true"><path d="M6.6 10.8a15 15 0 0 0 6.6 6.6l2.2-2.2c.3-.3.7-.4 1-.2 1.1.4 2.3.6 3.6.6.6 0 1 .4 1 1V20c0 .6-.4 1-1 1A17 17 0 0 1 3 4c0-.6.4-1 1-1h3.5c.6 0 1 .4 1 1 0 1.3.2 2.5.6 3.6.1.3 0 .7-.2 1z"/></svg>
        555-214-0386
      </li>
      <li>
        <svg viewBox="0 0 24 24" aria-hidden="true"><path d="M7 1h10a2 2 0 0 1 2 2v18a2 2 0 0 1-2 2H7a2 2 0 0 1-2-2V3a2 2 0 0 1 2-2zm0 3v15h10V4z"/></svg>
        555-610-2749
      </li>
      <li>
        <svg viewBox="0 0 24 24" aria-hidden="true"><path d="M2 5h20v14H2zm2 2v.5l8 5 8-5V7zm0 3v7h16v-7l-8 5z"/></svg>
        info@harrowfield.com
      </li>
      <li>
        <svg viewBox="0 0 24 24" aria-hidden="true"><path d="M12 2a10 10 0 1 0 0 20 10 10 0 0 0 0-20zm-1 17.9A8 8 0 0 1 4.2 10.2L9 15v1a2 2 0 0 0 2 2zm6.9-2.5A2 2 0 0 0 16 16h-1v-3a1 1 0 0 0-1-1H8v-2h2a1 1 0 0 0 1-1V7h2a2 2 0 0 0 2-2v-.4a8 8 0 0 1 2.9 12.8z"/></svg>
        www.harrowfield.com
      </li>
    </ul>
    <p class="address">
      <svg viewBox="0 0 12 16" aria-hidden="true"><path d="M6 15s5-5.2 5-9A5 5 0 0 0 1 6c0 3.8 5 9 5 9z"/><circle cx="6" cy="6" r="1.8"/></svg>
      1420 Birchwood Road, Fairbanks, Alaska 99701
    </p>
  </section>

  <section class="card card-back">
    <div class="brand">
      <span class="brand-dot"></span>
      <span class="brand-name">HARROWFIELD</span>
    </div>
  </section>
</main>
</body>
</html>
```